Infographic/Process Chart Style

Background: Our products have colours associated with them, in this instance, the red colour represents "web & digital/Web2Print" we also have other colours representing the other products and services (in the "something for everyone" service icons). This is explained further in the excerpts from our style guide attached.

The only devices that we've got in our style guide is this tear drop shape, ideally examples should continue to work with this shape

Deliverable:
We need a vector style for a step by step process, such as the web & digital website creation process attached. I've received several options from our agency but I'm not happy with any of them.

The style should look at a sequential process
- It should identify a standard steps
- A critical step and
- A final step.

Industry/Entity Type

Digital

```html
<!DOCTYPE html>
<html lang="en">
<head>
<meta charset="utf-8">
<title>Our Website Process</title>
<link rel="stylesheet" href="https://fonts.googleapis.com/css2?family=Arimo:wght@400;700&family=Roboto:wght@300&family=Roboto+Condensed:wght@400;700&display=swap">
<style>
  :root {
    --page: #fdfdfd;
    --brand-red: #ff1a00;
    --ink: #4a4a4a;
    --ink-soft: #5a5a5a;
    --white: #ffffff;
    --step-1: #7a0db8;
    --step-2: #f43b9c;
    --step-3: #f0b414;
    --step-4: #f5641c;
    --step-5: #f6581e;
    --step-6: #f21208;
    --neutral: #9a9a9a;
  }
  * { margin: 0; padding: 0; box-sizing: border-box; }
  html, body { width: 1200px; height: 849px; overflow: hidden; background: var(--page); }
  body { position: relative; font-family: "Arimo", Arial, sans-serif; color: var(--ink); }

  /* Masthead */
  .masthead { position: absolute; left: 39px; top: 40px; width: 1091px; height: 151px; display: flex; }
  .masthead-photo {
    width: 215px; height: 100%;
    background: linear-gradient(135deg, #eeeae6 0%, #d6d9db 40%, #6f7476 55%, #e6e6e3 80%, #f2f0ee 100%);
  }
  .masthead-band { position: relative; flex: 1; background: var(--brand-red); color: var(--white); }
  .page-title {
    position: absolute; left: 15px; top: 38px;
    font-family: "Roboto Condensed", Arial, sans-serif; font-weight: 400;
    font-size: 23px; line-height: 26px; text-transform: uppercase;
  }
  .section-nav {
    position: absolute; right: 13px; top: 28px; list-style: none; text-align: right;
    font-family: "Roboto Condensed", Arial, sans-serif; font-weight: 700;
    font-size: 8.6px; line-height: 13.8px; text-transform: uppercase; white-space: nowrap;
  }
  .section-nav .current { font-size: 11px; }

  /* Process */
  .process {
    position: absolute; left: 39px; top: 294px;
    display: grid; grid-template-columns: repeat(6, 140px) 145px; column-gap: 18.6px;
  }
  .step-drop {
    position: relative; width: 65px; height: 65px; margin: 0 auto;
    border-radius: 50% 0 50% 50%;
    color: var(--white); text-align: center; font-family: "Arimo", Arial, sans-serif; font-weight: 700;
    padding-top: 11px;
  }
  .step-drop small { display: block; font-size: 8.5px; line-height: 9px; text-transform: uppercase; }
  .step-drop b { display: block; font-size: 35px; line-height: 33px; }
  .step-title {
    height: 91px; margin-top: 16px; text-align: center; white-space: nowrap;
    font-family: "Roboto", Arial, sans-serif; font-weight: 300;
    font-size: 24px; line-height: 25px; color: var(--ink-soft);
  }
  .step-rule { border: 0; border-top: 1.5px dotted; margin-bottom: 14px; }
  .step-text { font-size: 15px; line-height: 20.8px; color: var(--ink); white-space: nowrap; letter-spacing: -0.1px; }

  .step--1 .step-drop { background: var(--step-1); } .step--1 .step-rule { border-color: var(--step-1); }
  .step--2 .step-drop { background: var(--step-2); } .step--2 .step-rule { border-color: var(--step-2); }
  .step--3 .step-drop { background: var(--step-3); } .step--3 .step-rule { border-color: var(--step-3); }
  .step--4 .step-drop { background: var(--step-4); } .step--4 .step-rule { border-color: var(--step-4); }
  .step--5 .step-drop { background: var(--step-5); } .step--5 .step-rule { border-color: var(--step-5); }
  .step--6 .step-drop { background: var(--step-6); } .step--6 .step-rule { border-color: var(--step-6); }

  /* Critical step: teardrop gets an outer ring, rule becomes a heavier dash */
  .step--critical .step-drop { box-shadow: 0 0 0 3px var(--page), 0 0 0 5.5px var(--step-5); }
  .step--critical .step-rule { border-top: 3px dashed var(--step-5); margin-top: -0.75px; margin-bottom: 12.5px; }

  /* Final step: teardrop carries a tick badge, rule becomes solid */
  .step--final .step-rule { border-top: 3px solid var(--step-6); margin-top: -0.75px; margin-bottom: 12.5px; }
  .done-badge {
    position: absolute; right: -8px; bottom: -4px; width: 24px; height: 24px;
    border-radius: 50%; background: var(--white); box-shadow: 0 0 0 2px var(--step-6);
    display: flex; align-items: center; justify-content: center;
  }

  /* Insight column */
  .insight-photo {
    width: 143px; height: 128px; margin-bottom: 44px;
    background: linear-gradient(90deg, #5e412c 0%, #a57c58 30%, #e8e2da 60%, #b99a7b 80%, #6d4f37 100%);
  }
  .insight .step-rule { border-color: var(--neutral); }
  .insight-lead { font-size: 10.8px; line-height: 16px; font-weight: 700; color: var(--ink-soft); margin-bottom: 8px; margin-top: 2px; white-space: nowrap; }
  .insight-list { list-style: none; font-size: 10.8px; line-height: 16px; font-weight: 700; color: var(--ink-soft); white-space: nowrap; }
  .insight-list li { position: relative; padding-left: 20px; margin-bottom: 9px; }
  .insight-list li::before { content: ">"; position: absolute; left: 0; font-weight: 400; }
</style>
</head>
<body>
  <header class="masthead">
    <div class="masthead-photo" role="img" aria-label="Photo of a woman working at a desktop computer"></div>
    <div class="masthead-band">
      <h1 class="page-title">Our<br>Website<br>Process</h1>
      <ul class="section-nav">
        <li>Why Swift Print for web &amp; digital</li>
        <li>Why you need to build your business online</li>
        <li>Ecommerce or info site?</li>
        <li>Mobile &amp; tablet websites</li>
        <li>The advantages of working with Swift Print</li>
        <li class="current">Our website process</li>
        <li>Case study</li>
      </ul>
    </div>
  </header>

  <main class="process">
    <section class="step step--1">
      <div class="step-drop"><small>Step</small><b>1</b></div>
      <h2 class="step-title">Brief &amp;<br>Consultation</h2>
      <hr class="step-rule">
      <p class="step-text">We get a feel for<br>what you need,<br>working with you to<br>compose the online<br>design brief.</p>
    </section>
    <section class="step step--2">
      <div class="step-drop"><small>Step</small><b>2</b></div>
      <h2 class="step-title">Concept<br>Creation</h2>
      <hr class="step-rule">
      <p class="step-text">We prepare a<br>collection of design<br>ideas for you to<br>choose from.</p>
    </section>
    <section class="step step--3">
      <div class="step-drop"><small>Step</small><b>3</b></div>
      <h2 class="step-title">Wireframe<br>Development</h2>
      <hr class="step-rule">
      <p class="step-text">Once you’ve settled<br>on a concept that<br>you like, we take<br>it one step further,<br>developing it into a<br>wireframe for you<br>to plan how the site<br>flows.</p>
    </section>
    <section class="step step--4">
      <div class="step-drop"><small>Step</small><b>4</b></div>
      <h2 class="step-title">Design &amp;<br>Content<br>Development</h2>
      <hr class="step-rule">
      <p class="step-text">Once this is signed<br>off we design and<br>create the content<br>for the entire site.</p>
    </section>
    <section class="step step--5 step--critical">
      <div class="step-drop"><small>Step</small><b>5</b></div>
      <h2 class="step-title">Feedback<br>&amp; Proofing</h2>
      <hr class="step-rule">
      <p class="step-text">As each element<br>takes shape, we’ll<br>check in with<br>you to make sure<br>we’re on brief.<br>This is the stage<br>where you proof,<br>provide feedback<br>and approve each<br>element.</p>
    </section>
    <section class="step step--6 step--final">
      <div class="step-drop"><small>Step</small><b>6</b>
        <span class="done-badge"><svg width="14" height="14" viewBox="0 0 14 14" aria-hidden="true"><path d="M2.5 7.5 L5.8 10.5 L11.5 3.8" fill="none" stroke="#f21208" stroke-width="2.4" stroke-linecap="round" stroke-linejoin="round"/></svg></span>
      </div>
      <h2 class="step-title">Building<br>&amp; Testing</h2>
      <hr class="step-rule">
      <p class="step-text">Hey presto – your<br>online campaign is<br>ready! Now we give it<br>to our code geeks to<br>build and test. Then<br>you can go LIVE!</p>
    </section>
    <aside class="step insight">
      <div class="insight-photo" role="img" aria-label="Photo of a smiling woman holding documents"></div>
      <hr class="step-rule">
      <p class="insight-lead">The three main areas<br>SMEs wish to improve their<br>online knowledge are:</p>
      <ul class="insight-list">
        <li>developing a web<br>presence (30%)</li>
        <li>utilising cloud based<br>solutions (25%)</li>
        <li>accepting payments<br>through websites (19%)</li>
      </ul>
    </aside>
  </main>
</body>
</html>
```